Poster for a Theatre production!

Create a poster (11 by 17) promoting an upcoming theatre production. The play is called THE HOLLOW LANTERN by Marcus T. Penwell . The play is a fusion of the absurd and realism and has a quantum physics/ mechanics slant fyi. I would like primarily a dark/black background with white print. there should be quantum physics imagery , (squiggly lines/ atoms etc. celestial even...) in the background as well . The
THE HOLLOW LANTERN letters Should Start out white as though ' painted ' (this is important.)and gradually fade to grey or white and black (Still visable though) . To be included also - 'Theatre Olvenk presents' (top of poster and about 1/3 the size) then THE HOLLOW LANTERN ' by Marcus T Penwell' and Half the size of the Title. Also included in print ' Directed by Gregor Lindqvist' and the words 'with' Margaret Solvane, Tim Orcutt and and Rosalind Petrakis Also in small print 'Video design by Corinne Valdez'. The poster also Needs the Dates ' Dec 7-16th ,The Fenwick Loft , 418 Marlowe Street 555 318-4096 '

Target Market(s)

Theatre going audience

Font styles to use
Other font styles liked:
• white painted effect on THE HOLLOW LANTERN

Colors
1b1b1b
fbfbfb
cbcbcb
dddddd
d5d5d5
5c5c5c
333333

Requirements
Must have
• Theatre Olvenk presents THE HOLLOW LANTERN by Marcus T Penwell . Directed by Gregor Lindqvist ( THIS THE CAST FYI)'with' Margaret Solvane, Tim Orcutt, Rosalynde Petrackis . Video design by Corinne Valdez. Dec 7-16th , The Fenwick Loft 418 Marlowe Street 555 318 4096 Black backgroud , painting effect on THE HOLLOW LANTERN . Quantum physics imagery background (SEE UP LOADED FILE) disregard human image
Nice to have
• IF YOU CAN INCORPORATE A HURTLING CHRISTMAS TREE THRU SPACE (RED & GREEN LIGHTS) THAT WOULD BE FANTASTiC see upload!! Christmas tree moving thru space as rocket..
Should not have
• COLOR -Except lights on Christmas tree

```html
<!DOCTYPE html>
<html lang="en">
<head>
<meta charset="utf-8">
<title>The Hollow Lantern — Theatre Olvenk</title>
<link rel="stylesheet" href="https://fonts.googleapis.com/css2?family=Rubik+Wet+Paint&family=Source+Sans+3:wght@400;600;700&display=swap">
<style>
  :root {
    --bg: #1e1e1e;
    --ink: #fbfbfb;
    --ink-soft: #dddddd;
    --grey-light: #cbcbcb;
    --grey-mid: #9a9a9a;
    --grey-dark: #5c5c5c;
    --grey-deep: #333333;
  }
  html, body {
    margin: 0;
    padding: 0;
    overflow: hidden;
    background: var(--bg);
  }
  .poster {
    position: relative;
    width: 777px;
    height: 1200px;
    background: var(--bg);
    color: var(--ink);
    font-family: "Source Sans 3", "Myriad Pro", Arial, sans-serif;
    overflow: hidden;
  }
  .centered {
    position: absolute;
    left: 0;
    width: 100%;
    text-align: center;
    margin: 0;
    line-height: 1;
  }
  .company {
    top: 52px;
    font-size: 50px;
    font-weight: 700;
    letter-spacing: -0.5px;
  }
  .presents {
    top: 118px;
    font-size: 30px;
    font-weight: 400;
  }
  .title {
    margin: 0;
  }
  .title__line {
    position: absolute;
    left: 0;
    width: 100%;
    text-align: center;
    line-height: 1;
    font-family: "Rubik Wet Paint", "Rubik", Impact, sans-serif;
    font-weight: 400;
    text-transform: uppercase;
    color: transparent;
    -webkit-background-clip: text;
    background-clip: text;
    transform-origin: 50% 0;
    white-space: nowrap;
  }
  .title__line--1 {
    top: 138px;
    font-size: 120px;
    transform: scaleY(1.45);
    background-image: linear-gradient(180deg, var(--ink) 0%, #f3f3f3 100%);
  }
  .title__line--2 {
    top: 268px;
    font-size: 115px;
    letter-spacing: 6px;
    transform: scaleY(1.6);
    background-image: linear-gradient(180deg, #f0f0f0 0%, var(--ink-soft) 60%, var(--grey-light) 100%);
  }
  .title__line--3 {
    top: 392px;
    font-size: 110px;
    letter-spacing: 8px;
    transform: scaleY(2.1);
    background-image: linear-gradient(180deg, #c4c4c4 0%, #8e8e8e 55%, var(--grey-dark) 100%);
  }
  .author {
    top: 664px;
    font-size: 35px;
    font-weight: 700;
  }
  .director {
    top: 716px;
    font-size: 21px;
    font-weight: 700;
  }
  .cast {
    top: 745px;
    font-size: 22px;
    font-weight: 400;
  }
  .video {
    top: 775px;
    font-size: 22px;
    font-weight: 400;
  }
  .tiles {
    position: absolute;
    top: 822px;
    left: 25px;
    display: flex;
    gap: 10px;
  }
  .tile {
    width: 170px;
    height: 166px;
    border: 2px solid var(--ink);
  }
  .tile--grid { background: radial-gradient(circle at 40% 45%, #6a6a6a 0%, var(--grey-deep) 55%, #111 100%); }
  .tile--tunnel { background: radial-gradient(ellipse at 50% 70%, var(--ink) 0%, #8a8a8a 30%, var(--grey-deep) 75%, #151515 100%); }
  .tile--swirl { background: linear-gradient(135deg, #7a7a7a 0%, var(--grey-deep) 55%, #1a1a1a 100%); }
  .tile--stars { background: radial-gradient(circle at 60% 40%, #4a4a4a 0%, #222 70%, #111 100%); }
  .dates {
    top: 1032px;
    font-size: 42px;
    font-weight: 700;
    color: var(--grey-mid);
  }
  .venue {
    top: 1082px;
    font-size: 24px;
    font-weight: 700;
    color: var(--grey-mid);
  }
  .phone {
    top: 1117px;
    font-size: 31px;
    font-weight: 700;
    color: var(--grey-mid);
  }
</style>
</head>
<body>
<main class="poster">
  <p class="centered company">Theatre Olvenk</p>
  <p class="centered presents">Presents</p>

  <h1 class="title" aria-label="The Hollow Lantern">
    <span class="title__line title__line--1" aria-hidden="true">The</span>
    <span class="title__line title__line--2" aria-hidden="true">Hollow</span>
    <span class="title__line title__line--3" aria-hidden="true">Lantern</span>
  </h1>

  <p class="centered author">By Marcus T. Penwell</p>
  <p class="centered director">Directed by Gregor Lindqvist</p>
  <p class="centered cast">With Margaret Solvane, Tim Orcutt and Rosalind Petrakis</p>
  <p class="centered video">Video Design by Corinne Valdez</p>

  <div class="tiles">
    <div class="tile tile--grid" role="img" aria-label="Quantum imagery: curved grid lines over a misty field"></div>
    <div class="tile tile--tunnel" role="img" aria-label="Quantum imagery: glowing spacetime funnel"></div>
    <div class="tile tile--swirl" role="img" aria-label="Quantum imagery: swirling light trails across a grid"></div>
    <div class="tile tile--stars" role="img" aria-label="Quantum imagery: star field with faint grid lines"></div>
  </div>

  <p class="centered dates">December 7 - 16, 2017</p>
  <p class="centered venue">The Fenwick Loft | 418 Marlowe Street | Harrowgate, Ontario</p>
  <p class="centered phone">555.318.4096</p>
</main>
</body>
</html>
```